Business Card Re-Design

Consulting Company: To build a high performance organization, you need great leaders at all levels throughout your organization. The Northvale Talent Growth Studio engages, inspires, and educates current and future leaders to step beyond the ordinary and deliver exceptional results. This new breed of leaders will motivate your staff to leave the safety of complacency behind and come together to build an extraordinary organization. The current trend has been to ask our people to do more with fewer resources. People have been stepping up to the challenge, but more is required to ensure success with a new work paradigm. We work with your management team to build a successful strategy that will make your organization more effective. NTGS then supports your management team by providing a comprehensive set of proven services to empower your entire organization to successfully execute new strategies.Let NTGS help you optimize your organization’s individual and team performance today!

Target Market(s)

Federal, State and Local Government / Non profit

Industry/Entity Type

Management Consulting

Contact Information for Business Card

NTGS, inc (Northvale Talent Growth Studio) Optimizing Individual and Organizational Performance

Colors
fee18a
ec1f27
474747
fbf289

Requirements
Must have
• Professional and high quality feel

```html
<!DOCTYPE html>
<html lang="en">
<head>
<meta charset="utf-8">
<title>NTGS, inc — Business Card</title>
<link rel="stylesheet" href="https://fonts.googleapis.com/css2?family=Montserrat:wght@500;600;700;800&family=Arimo:wght@400&display=swap">
<style>
  :root {
    --card-bg: #383737;
    --brand-charcoal: #474747;
    --band-name: #545150;
    --band-contact: #858585;
    --accent-gold: #fee18a;
    --accent-red: #ec1f27;
    --accent-lemon: #fbf289;
    --ink-white: #ffffff;
    --ink-logo: #d3d3d3;
    --ink-title: #8c8a89;
  }
  * { margin: 0; padding: 0; box-sizing: border-box; }
  html, body { width: 720px; height: 1200px; overflow: hidden; background: var(--card-bg); }
  .card {
    position: relative;
    width: 720px;
    height: 1200px;
    background: var(--card-bg);
    overflow: hidden;
    font-family: "Arimo", Arial, sans-serif;
    color: var(--ink-white);
  }
  .team-backdrop {
    position: absolute;
    left: 139px; top: 32px;
    width: 458px; height: 469px;
    background: radial-gradient(ellipse closest-side at 50% 50%, var(--brand-charcoal) 0%, rgba(71,71,71,0.5) 60%, rgba(56,55,55,0) 100%);
  }
  .bands { position: absolute; inset: 0; }
  .brand {
    position: absolute;
    left: 200px; top: 86px;
    font-family: "Montserrat", sans-serif;
    font-weight: 700;
    color: var(--ink-logo);
  }
  .brand-line {
    font-size: 22px;
    letter-spacing: 5px;
    line-height: 26px;
  }
  .brand-mark {
    font-size: 122px;
    line-height: 150px;
    letter-spacing: -3px;
    margin-left: -6px;
  }
  .brand-tail {
    font-size: 15px;
    letter-spacing: 4px;
    line-height: 20px;
    margin-left: 160px;
  }
  .accent-rule {
    width: 120px;
    height: 4px;
    margin: 10px 0 0 160px;
    background: var(--accent-gold);
  }
  .tilted {
    position: absolute;
    display: flex;
    align-items: center;
    white-space: nowrap;
    transform: rotate(-14.7deg);
    transform-origin: 0 50%;
  }
  .person-name {
    left: 74px; top: 656px; height: 60px;
    font-family: "Montserrat", sans-serif;
    font-weight: 600;
    font-size: 50px;
    letter-spacing: 12px;
  }
  .person-title {
    left: 190px; top: 690px; height: 32px;
    font-family: "Montserrat", sans-serif;
    font-weight: 700;
    font-size: 27px;
    letter-spacing: 7px;
    color: var(--ink-title);
  }
  .contact {
    font-size: 33px;
    gap: 12px;
  }
  .contact svg { flex: none; fill: var(--accent-gold); }
  .contact-mobile { left: 142px; top: 801px; height: 44px; }
  .contact-fax { left: 42px; top: 931px; height: 44px; }
  .contact-email { margin-left: 36px; }
  .contact-address { left: 18px; top: 1058px; height: 44px; }
  .contact-item { display: flex; align-items: center; gap: 12px; }
</style>
</head>
<body>
  <div class="card">
    <div class="team-backdrop" role="img" aria-label="Soft silhouettes of a group of standing people behind the company name"></div>

    <svg class="bands" width="720" height="1200" viewBox="0 0 720 1200" aria-hidden="true">
      <polygon points="0,653 720,464 720,613 0,802" fill="var(--band-name)"/>
      <polygon points="0,816 720,624 720,723 0,912" fill="var(--band-contact)"/>
      <polygon points="0,926 720,736 720,832 0,1019" fill="var(--band-contact)"/>
      <polygon points="0,1033 720,846 720,939 0,1131" fill="var(--band-contact)"/>
    </svg>

    <div class="brand">
      <div class="brand-line">NORTHVALE</div>
      <div class="brand-line">TALENT</div>
      <div class="brand-mark">NTGS</div>
      <div class="brand-tail">GROWTH</div>
      <div class="brand-tail">STUDIO, INC</div>
      <div class="accent-rule"></div>
    </div>

    <div class="tilted person-name">OWEN R.DALTON</div>
    <div class="tilted person-title">PRESIDENT / CEO</div>

    <div class="tilted contact contact-mobile">
      <svg width="24" height="38" viewBox="0 0 24 38" aria-hidden="true">
        <path d="M4 0h16a4 4 0 0 1 4 4v30a4 4 0 0 1-4 4H4a4 4 0 0 1-4-4V4a4 4 0 0 1 4-4zm0 5v25h16V5zm8 27a2 2 0 1 0 0 4 2 2 0 0 0 0-4z"/>
      </svg>
      <span>410.555.0176</span>
    </div>

    <div class="tilted contact contact-fax">
      <span class="contact-item">
        <svg width="42" height="38" viewBox="0 0 42 38" aria-hidden="true">
          <path d="M10 0h22v10h-4V4H14v6h-4zM4 12h34a4 4 0 0 1 4 4v14h-8v-4H8v4H0V16a4 4 0 0 1 4-4zm8 18h18v8H12z"/>
          <rect x="13" y="29" width="16" height="8" fill="var(--band-contact)"/>
        </svg>
        <span>410.555.0182</span>
      </span>
      <span class="contact-item contact-email">
        <svg width="42" height="28" viewBox="0 0 42 28" aria-hidden="true">
          <rect width="42" height="28" rx="2"/>
          <path d="M2 3l19 14L40 3" fill="none" stroke="var(--band-contact)" stroke-width="1.5"/>
        </svg>
        <span>owen@ntgs.co</span>
      </span>
    </div>

    <div class="tilted contact contact-address">
      <svg width="32" height="30" viewBox="0 0 32 30" aria-hidden="true">
        <path d="M16 0l16 15h-5v15h-7v-9h-8v9H5V15H0z"/>
      </svg>
      <span>2250 Larkspur Crest Fernwick, MD 20999</span>
    </div>
  </div>
</body>
</html>
```